KAVRO iOS app needs a fun consumer interface design

KAVRO is a file transfer app aimed at consumers to help them get files onto their iOS devices. The app is based around each user having a personalised upload web address, and the ability to issue temporary time limited upload codes to friends and colleagues that they can use to send them files. The first version is already live in the app store but we are working on a second, simplified version. You can see the screen shots for this on www.kavro-example.com and I have attached a quick guide to app flow. The app now looks like a standard templated iOS 7 app. We need a design for the app that give it its own look, whilst retaining the standard iOS cues. It needs to look good on iPhone and iPad. We have a far east techno feel to the app at the moment with our characters, and we want to keep the logo. The website is currently a simple template, there's an ongoing competition to redesign that too - http://jobs.pixelbidhub.example/job.aspx?id=318264
We have a working app with a reasonable design - we are looking for someone to take that design, add the polish a professional designer can bring, to make it pixel perfect and stand out as an app that has great design as well as great functionality.
We are also looking for something that works well on iPhone and iPad. See the attached screenshots of the iPad version - we want that version to look beautiful, not the big empty screen it is now.
Updates
Thanks for the designs so far, they look good. Could you draw them up for iPad size screens too please. The signup/login page and new code pages I think need the most attention as each page doesn't collect that much information, and so a lot of the screen is currently blank. I think we need some sort of background to set the content into for these pages.
The old app is installable for free from the App store if that helps you get a feel for it on the iPad.
Target Market(s)
Consumers, techno savvy
Industry/Entity Type
Store
Font styles to use
Look and feel

```html
<!DOCTYPE html>
<html lang="en">
<head>
<meta charset="utf-8">
<title>KAVRO – Upload code history</title>
<link href="https://fonts.googleapis.com/css2?family=Roboto:wght@300;400;500&display=swap" rel="stylesheet">
<style>
  :root {
    --bar-blue: #29a8e0;
    --button-blue: #1787c2;
    --title-blue: #1e8fcf;
    --white: #ffffff;
    --row-title: #5a5a5a;
    --row-meta: #a8a8a8;
    --divider: #e2e2e2;
    --chevron: #8a8a8a;
    --strip-1: #b83d6c;
    --strip-2: #ea3a6e;
    --strip-3: #f27a30;
    --strip-4: #fdb942;
    --strip-5: #5fc3c5;
    --strip-6: #47a9a6;
    --strip-7: #a3cf3e;
    --strip-8: #d0ea8b;
  }
  * { box-sizing: border-box; margin: 0; padding: 0; }
  html, body { width: 1200px; height: 2282px; overflow: hidden; background: #ffffff; }
  body { font-family: "Roboto", Arial, sans-serif; position: relative; }

  .status-bar {
    position: absolute; left: 0; top: 0; width: 1200px; height: 72px;
    background: var(--bar-blue); color: var(--white);
    font-size: 40px; font-weight: 400;
  }
  .status-bar .signal { position: absolute; left: 26px; top: 14px; display: flex; align-items: center; gap: 30px; }
  .status-bar .signal svg { display: block; }
  .status-bar .carrier { margin-left: -14px; }
  .status-bar .wifi { position: absolute; left: 362px; top: 20px; }
  .status-bar .clock { position: absolute; left: 0; width: 1200px; top: 14px; text-align: center; }
  .status-bar .battery { position: absolute; right: 20px; top: 14px; display: flex; align-items: center; gap: 12px; }

  .nav-bar {
    position: absolute; left: 0; top: 72px; width: 1200px; height: 172px;
    background: var(--bar-blue);
    box-shadow: 0 4px 6px rgba(0,0,0,0.12);
    z-index: 2;
  }
  .back-button {
    position: absolute; left: 20px; top: 48px; width: 112px; height: 103px;
    background: var(--button-blue); border-radius: 4px;
    box-shadow: 0 3px 4px rgba(0,0,0,0.18);
    display: flex; align-items: center; justify-content: center;
  }
  .code-title {
    position: absolute; left: 279px; top: 46px; width: 634px; height: 106px;
    background: var(--white); border-radius: 16px;
    box-shadow: 0 3px 4px rgba(0,0,0,0.15);
    color: var(--title-blue); font-size: 54px; font-weight: 400; letter-spacing: 1px;
    display: flex; align-items: center; justify-content: center;
  }

  .upload-list { position: absolute; left: 0; top: 244px; width: 1200px; list-style: none; background: var(--white); z-index: 1; }
  .upload-row { position: relative; height: 224px; border-bottom: 2px solid var(--divider); }
  .file-icon { position: absolute; left: 52px; top: 45px; width: 132px; height: 132px; }
  .upload-time { position: absolute; left: 284px; top: 52px; font-size: 58px; font-weight: 300; color: var(--row-title); }
  .upload-meta { position: absolute; left: 284px; top: 134px; font-size: 34px; font-weight: 400; color: var(--row-meta); }
  .chevron { position: absolute; left: 1114px; top: 88px; }

  .backdrop {
    position: absolute; left: 0; top: 916px; width: 1200px; height: 1274px;
    background:
      radial-gradient(ellipse 500px 400px at 540px 160px, rgba(236,212,208,0.9), transparent 70%),
      radial-gradient(ellipse 420px 460px at 120px 500px, rgba(240,236,234,0.9), transparent 70%),
      radial-gradient(ellipse 380px 400px at 1100px 200px, rgba(244,247,247,1), transparent 70%),
      linear-gradient(180deg, #eceaea 0%, #e2e1e3 45%, #e6e6e8 80%, #f1f1f1 100%);
  }

  .colour-strip { position: absolute; left: 0; bottom: 0; width: 1200px; height: 92px; display: flex; }
  .colour-strip span { flex: 1; }
  .colour-strip span:nth-child(1) { background: var(--strip-1); }
  .colour-strip span:nth-child(2) { background: var(--strip-2); }
  .colour-strip span:nth-child(3) { background: var(--strip-3); }
  .colour-strip span:nth-child(4) { background: var(--strip-4); }
  .colour-strip span:nth-child(5) { background: var(--strip-5); }
  .colour-strip span:nth-child(6) { background: var(--strip-6); }
  .colour-strip span:nth-child(7) { background: var(--strip-7); }
  .colour-strip span:nth-child(8) { background: var(--strip-8); }
</style>
</head>
<body>

<header class="status-bar">
  <div class="signal">
    <svg width="150" height="30" viewBox="0 0 150 30" aria-hidden="true">
      <circle cx="13" cy="15" r="11" fill="#fff"/>
      <circle cx="42" cy="15" r="11" fill="#fff"/>
      <circle cx="71" cy="15" r="11" fill="#fff"/>
      <circle cx="100" cy="15" r="10" fill="none" stroke="#fff" stroke-width="2.5"/>
      <circle cx="129" cy="15" r="10" fill="none" stroke="#fff" stroke-width="2.5"/>
    </svg>
    <span class="carrier">Nuvell</span>
  </div>
  <svg class="wifi" width="44" height="34" viewBox="0 0 44 34" aria-hidden="true">
    <path d="M22 32 L14 24 A11 11 0 0 1 30 24 Z" fill="#fff"/>
    <path d="M8 18 A20 20 0 0 1 36 18" fill="none" stroke="#fff" stroke-width="5"/>
    <path d="M2 11 A28 28 0 0 1 42 11" fill="none" stroke="#fff" stroke-width="5"/>
  </svg>
  <div class="clock">4:21 PM</div>
  <div class="battery">
    <span>100%</span>
    <svg width="90" height="36" viewBox="0 0 90 36" aria-hidden="true">
      <rect x="2" y="2" width="78" height="32" rx="5" fill="none" stroke="#fff" stroke-width="3"/>
      <rect x="7" y="7" width="68" height="22" rx="2" fill="#fff"/>
      <rect x="82" y="12" width="6" height="12" rx="2" fill="#fff"/>
    </svg>
  </div>
</header>

<nav class="nav-bar">
  <div class="back-button" aria-label="Back">
    <svg width="30" height="46" viewBox="0 0 30 46" aria-hidden="true">
      <path d="M24 6 L8 23 L24 40" fill="none" stroke="#fff" stroke-width="6" stroke-linecap="round" stroke-linejoin="round"/>
    </svg>
  </div>
  <h1 class="code-title">YASIGRHB</h1>
</nav>

<ul class="upload-list">
  <li class="upload-row">
    <svg class="file-icon" viewBox="0 0 132 132" role="img" aria-label="Received file icon">
      <defs>
        <linearGradient id="icon-fill" x1="0" y1="0" x2="0" y2="1">
          <stop offset="0" stop-color="#d6eefa"/>
          <stop offset="1" stop-color="#8fd0f1"/>
        </linearGradient>
      </defs>
      <circle cx="66" cy="66" r="62" fill="url(#icon-fill)" stroke="#4aaee0" stroke-width="4"/>
    </svg>
    <div class="upload-time">Today 20:42</div>
    <div class="upload-meta">52.14 kB (91.125.9.32)</div>
    <svg class="chevron" width="32" height="52" viewBox="0 0 32 52" aria-hidden="true">
      <path d="M6 4 L26 26 L6 48" fill="none" stroke="var(--chevron)" stroke-width="4"/>
    </svg>
  </li>
  <li class="upload-row">
    <svg class="file-icon" viewBox="0 0 132 132" role="img" aria-label="Received file icon">
      <circle cx="66" cy="66" r="62" fill="url(#icon-fill)" stroke="#4aaee0" stroke-width="4"/>
    </svg>
    <div class="upload-time">Yesterday 16:50</div>
    <div class="upload-meta">52.14 kB (91.125.9.32)</div>
    <svg class="chevron" width="32" height="52" viewBox="0 0 32 52" aria-hidden="true">
      <path d="M6 4 L26 26 L6 48" fill="none" stroke="var(--chevron)" stroke-width="4"/>
    </svg>
  </li>
  <li class="upload-row">
    <svg class="file-icon" viewBox="0 0 132 132" role="img" aria-label="Received file icon">
      <circle cx="66" cy="66" r="62" fill="url(#icon-fill)" stroke="#4aaee0" stroke-width="4"/>
    </svg>
    <div class="upload-time">Yesterday 16:50</div>
    <div class="upload-meta">52.14 kB (91.125.9.32)</div>
    <svg class="chevron" width="32" height="52" viewBox="0 0 32 52" aria-hidden="true">
      <path d="M6 4 L26 26 L6 48" fill="none" stroke="var(--chevron)" stroke-width="4"/>
    </svg>
  </li>
</ul>

<div class="backdrop" role="img" aria-label="Soft blurred background image in pale pink and grey tones"></div>

<footer class="colour-strip" aria-hidden="true">
  <span></span><span></span><span></span><span></span>
  <span></span><span></span><span></span><span></span>
</footer>

</body>
</html>
```